Looking for a contemporary business card design with our logo

would like to consider a embossing look although I'm not married to the idea. We are a custom jeweler that needs a look that represents old world craftsmanship with a modern twist that's why we went with a more modern shield type of logo that can be stamped inside our rings.
It could be two sided or one we are more after a look the pops and is trendy and creative. (WE ARE NOT LOOKING FOR A COOKIE CUTTER LAYOUT)
We have attached the image and will be using the logo with harwick studio wording in the format that it's in unless you see a better way of doing it.
If the logo needs a twist we are O.K. with suggestions as well.
This card should scream "Quality" from a high end studio.
Harwick Studio
4186 Maplecrest Rd. Unit B-2
Alderbrook, NV 80317
www.harwickstudio-example.com
lu@harwickstudio-example.com
Should speak quality craftsmanship

```html
<!DOCTYPE html>
<html lang="en">
<head>
<meta charset="utf-8">
<title>Harwick Studio – Business Card</title>
<link rel="stylesheet" href="https://fonts.googleapis.com/css2?family=Open+Sans:wght@400;700&display=swap">
<style>
  :root {
    --backdrop: #2b2b2b;
    --card-light: #e4e4e4;
    --card-mid: #cdcdcd;
    --ink: #1c1c1c;
    --panel: #0d0d0d;
    --panel-text: #f2f2f2;
    --icon-bg: #e8e8e8;
  }
  * { margin: 0; padding: 0; box-sizing: border-box; }
  html, body {
    width: 1200px;
    height: 797px;
    overflow: hidden;
    background: var(--backdrop);
    font-family: "Open Sans", Arial, sans-serif;
  }
  .stage {
    width: 1200px;
    height: 797px;
    display: flex;
    align-items: center;
    justify-content: center;
  }
  .business-card {
    position: relative;
    width: 840px;
    height: 480px;
    background: linear-gradient(135deg, var(--card-light), var(--card-mid));
    box-shadow: 0 6px 0 #1a1a1a, 0 18px 40px rgba(0,0,0,0.45);
  }
  .brand {
    position: absolute;
    left: 64px;
    top: 110px;
    width: 320px;
    display: flex;
    flex-direction: column;
    align-items: flex-start;
    gap: 18px;
  }
  .brand-name {
    font-weight: 700;
    font-size: 30px;
    line-height: 1.1;
    color: var(--ink);
    text-transform: uppercase;
    letter-spacing: 1px;
    white-space: nowrap;
  }
  .brand-square {
    width: 210px;
    height: 210px;
    background: var(--ink);
  }
  .contact-panel {
    position: absolute;
    left: 400px;
    right: 34px;
    top: 48px;
    bottom: 148px;
    background: var(--panel);
    color: var(--panel-text);
    padding: 60px 30px 0 40px;
    font-size: 19px;
    line-height: 1.3;
    letter-spacing: 0.4px;
  }
  .company-name { font-weight: 700; }
  .address { margin-bottom: 30px; }
  .contact-list { list-style: none; }
  .contact-list li {
    display: flex;
    align-items: center;
    gap: 14px;
    margin-bottom: 2px;
    white-space: nowrap;
  }
  .contact-icon {
    width: 18px;
    height: 18px;
    flex: none;
  }
</style>
</head>
<body>
<main class="stage">
  <article class="business-card">
    <div class="brand">
      <div class="brand-name">Harwick Studio</div>
      <div class="brand-square"></div>
    </div>

    <section class="contact-panel">
      <div class="company-name">Harwick Studio</div>
      <div class="address">4186 Maplecrest Rd. Unit B-2<br>Alderbrook, NV 80317</div>
      <ul class="contact-list">
        <li>
          <svg class="contact-icon" viewBox="0 0 18 18" aria-hidden="true">
            <rect width="18" height="18" rx="3" fill="var(--icon-bg)"/>
            <path d="M5 4.5 L7 4.5 L8 7 L6.8 8 Q8 10.5 10 11.2 L11 10 L13.5 11 L13.5 13 Q12.5 14 11 13.8 Q6 12.5 4.3 7 Q4.2 5.3 5 4.5Z" fill="var(--panel)"/>
          </svg>
          <span>555-201-4478</span>
        </li>
        <li>
          <svg class="contact-icon" viewBox="0 0 18 18" aria-hidden="true">
            <rect width="18" height="18" rx="3" fill="var(--icon-bg)"/>
            <rect x="4" y="5.5" width="10" height="7" fill="none" stroke="var(--panel)" stroke-width="1.4"/>
            <path d="M4 5.5 L9 9.5 L14 5.5" fill="none" stroke="var(--panel)" stroke-width="1.4"/>
          </svg>
          <span>lu@harwickstudio-example.com</span>
        </li>
        <li>
          <svg class="contact-icon" viewBox="0 0 18 18" aria-hidden="true">
            <rect width="18" height="18" rx="3" fill="var(--icon-bg)"/>
            <circle cx="9" cy="9" r="5" fill="none" stroke="var(--panel)" stroke-width="1.3"/>
            <ellipse cx="9" cy="9" rx="2.2" ry="5" fill="none" stroke="var(--panel)" stroke-width="1.1"/>
            <line x1="4" y1="9" x2="14" y2="9" stroke="var(--panel)" stroke-width="1.1"/>
          </svg>
          <span>www.harwickstudio-example.com</span>
        </li>
      </ul>
    </section>
  </article>
</main>
</body>
</html>
```